Label For Hand soap

Hello,

I would like to get your assistance with creating a label for my hand soap that I am in the process of developing. I would like the label to look simple visually appealing and eye catching similar to a cologne bottle's label. I would like there to be graphic or illustration accompanied with the text. The color scheme is black. I would like the background of the label to be transparent so that I can show the color of my product. I have attached some pictures of my bottle and some labels that I like for your reference. The name of my brand is Velor. The hand soap scent is candied pineapples.

Thanks

```html
<!DOCTYPE html>
<html lang="en">
<head>
<meta charset="utf-8">
<title>Velor Hand Wash Label</title>
<link href="https://fonts.googleapis.com/css2?family=Literata:opsz,wght@7..72,400;7..72,600;7..72,700&display=swap" rel="stylesheet">
<style>
  :root {
    --product-amber: #f4a00c;
    --ornament-dark: #5a3606;
    --ornament-mid: #b0700a;
    --ink: #111111;
  }
  * { margin: 0; padding: 0; box-sizing: border-box; }
  html, body {
    width: 1200px;
    height: 1200px;
    overflow: hidden;
  }
  body {
    background: var(--product-amber);
    font-family: "Literata", Georgia, serif;
    color: var(--ink);
  }
  .label {
    position: relative;
    width: 1200px;
    height: 1200px;
  }
  .monogram {
    position: absolute;
    left: 485px;
    top: 188px;
    width: 230px;
    height: 357px;
  }
  .brand-name,
  .product-type,
  .scent,
  .volume {
    position: absolute;
    left: 0;
    width: 100%;
    text-align: center;
    line-height: 1;
  }
  .brand-name {
    top: 548px;
    font-size: 104px;
    font-weight: 700;
    letter-spacing: 1px;
  }
  .product-type {
    top: 722px;
    font-size: 64px;
    font-weight: 400;
  }
  .scent {
    top: 796px;
    font-size: 36px;
    font-weight: 600;
  }
  .volume {
    top: 975px;
    font-size: 36px;
    font-weight: 600;
  }
</style>
</head>
<body>
  <main class="label">
    <svg class="monogram" viewBox="0 0 230 357" role="img" aria-label="Ornate decorative initial monogram in black filigree">
      <defs>
        <radialGradient id="ornament-glow" cx="50%" cy="50%" r="55%">
          <stop offset="0%" stop-color="var(--ornament-dark)" stop-opacity="0.55"/>
          <stop offset="60%" stop-color="var(--ornament-mid)" stop-opacity="0.35"/>
          <stop offset="100%" stop-color="var(--ornament-mid)" stop-opacity="0"/>
        </radialGradient>
      </defs>
      <ellipse cx="115" cy="178" rx="115" ry="178" fill="url(#ornament-glow)"/>
    </svg>
    <h1 class="brand-name">Velor</h1>
    <p class="product-type">Hand Wash</p>
    <p class="scent">Candied Pineapples</p>
    <p class="volume">250 ml</p>
  </main>
</body>
</html>
```